New corporate Powerpoint template *

Hi,
We would like to have one new corporate Powerpoint template which can be used for various presentations (Sales, Investors, Marketing, Engineers, HR, Corporate presentations…) Please note that this template will be used for both internal and external presentations.
Please take a look at our website to get a feel for our branding.
https://www.brenvar-microtech.example/

Some visual elements to include:

• The theme needs to be relevant to our industry i.e. Semiconductor theme (circuit board/chip graphic elements)
• Simple uses of color, lifestyle images, moving away from Geometric patterns and colorful wave
• Style should be modern, clean and gender neutral
• Use Korvet blue as more of an accent color - Avoid the overuse of blue (seems a little too bright sometimes)
• Korvet logo to appear on every page

Necessary slides to include:
• Cover Slide
• Agenda Slide
• Divider / Title Slide
• Content Slide
• White Slide
• Comparison slide (two, three, four)
• Table slide with the ability to add rows/columns
• Timeline/roadmap slide
• End Slide

Target Market(s)

Semiconductor industry

Font styles to use
Other font styles liked:
• Arial or Rockwell

Colors
33a6d7

Requirements
Must have
• • The theme needs to be relevant to our industry i.e. Semiconductor theme (circuit board/chip graphic elements)
• • Simple uses of color, lifestyle images
• • Style should be modern, clean and gender neutral
• • Use Korvet blue as more of an accent color
• • Korvet logo to appear on every page
• Necessary slides to include:
• • Cover Slide
• • Agenda Slide
• • Divider / Title Slide
• • Content Slide
• • White Slide
• • Comparison slide (two, three, four)
• • Table slide with the ability to add rows/columns
• • Timeline/roadmap slide
• • End Slide
Nice to have
Should not have
• - Avoid the overuse of blue (seems a little too bright sometimes)
• - Do not use any kind of wave as a graphic

```html
<!DOCTYPE html>
<html lang="en">
<head>
<meta charset="utf-8">
<title>Korvet corporate presentation template</title>
<link href="https://fonts.googleapis.com/css2?family=Arimo:wght@400;700&display=swap" rel="stylesheet">
<style>
  :root{
    --stage:#3a3a3a;
    --paper:#ffffff;
    --blue:#33a6d7;
    --blue-deep:#2a93c6;
    --sky:#5bc0d6;
    --teal:#21948c;
    --green:#8cc63f;
    --grey:#6d6d6d;
    --grey-mid:#8a8a8a;
    --ink:#333333;
    --soft:#efefef;
    --line-soft:#bfe3f2;
  }
  html,body{margin:0;padding:0;overflow:hidden;}
  body{width:1200px;height:930px;background:var(--stage);position:relative;font-family:"Arimo",Arial,sans-serif;}
  .slide{position:absolute;width:368.8px;height:207.2px;background:var(--paper);display:block;}
  .row-1{top:38.4px}.row-2{top:254.4px}.row-3{top:469.6px}.row-4{top:684.8px}
  .col-1{left:38.4px}.col-2{left:415.2px}.col-3{left:792px}
  .col-4a{left:226.4px}.col-4b{left:603.2px}

  text{font-family:"Arimo",Arial,sans-serif;}
  .f-blue{fill:var(--blue)}.f-deep{fill:var(--blue-deep)}.f-sky{fill:var(--sky)}
  .f-teal{fill:var(--teal)}.f-green{fill:var(--green)}.f-grey{fill:var(--grey)}
  .f-ink{fill:var(--ink)}.f-white{fill:#fff}.f-soft{fill:var(--soft)}
  .s-blue{stroke:var(--blue)}.s-teal{stroke:var(--teal)}.s-green{stroke:var(--green)}
  .s-grey{stroke:var(--grey-mid)}.s-soft{stroke:var(--line-soft)}

  .brand-name{fill:var(--blue);font-weight:400;}
  .slide-title{font-size:11.5px;letter-spacing:3.6px;fill:var(--ink);}
  .divider-number{font-size:54px;font-weight:400;}
  .divider-label{font-size:11px;letter-spacing:3.4px;fill:var(--ink);}
  .caption{font-size:4.6px;fill:#555;}
  .cell-text{font-size:5px;fill:#555;}
  .menu-item{font-size:11px;font-weight:700;letter-spacing:1.6px;}
  .year{font-size:7.5px;letter-spacing:2.6px;}
  .head-text{font-size:7px;fill:#fff;letter-spacing:0.6px;}
</style>
</head>
<body>

<svg width="0" height="0" style="position:absolute" aria-hidden="true">
  <defs>
    <linearGradient id="footer-fade" x1="0" x2="1" y1="0" y2="0">
      <stop offset="0" stop-color="#ffffff"/>
      <stop offset="1" stop-color="#d8eef8"/>
    </linearGradient>
    <radialGradient id="ring-fade" cx="0.5" cy="0.5" r="0.5">
      <stop offset="0" stop-color="#ffffff"/>
      <stop offset="0.55" stop-color="#ffffff"/>
      <stop offset="0.8" stop-color="#dff1f9"/>
      <stop offset="1" stop-color="#ffffff"/>
    </radialGradient>
    <symbol id="brand-small" viewBox="0 0 70 18">
      <circle cx="7" cy="10" r="6" class="f-blue"/>
      <text x="16" y="15" font-size="16" class="brand-name">korvet</text>
    </symbol>
  </defs>
</svg>

<!-- Cover -->
<svg class="slide row-1 col-1" viewBox="0 0 461 259">
  <rect x="64" y="54" width="317" height="28" fill="#bdbdbd"/>
  <defs>
    <linearGradient id="cover-photo" x1="0" x2="1" y1="0" y2="1">
      <stop offset="0" stop-color="#1d2c3a"/>
      <stop offset="0.45" stop-color="#1f6a80"/>
      <stop offset="1" stop-color="#0f3a4c"/>
    </linearGradient>
  </defs>
  <rect x="0" y="82" width="461" height="100" fill="url(#cover-photo)" role="img" aria-label="Close-up photo of probes testing a circuit board"/>
  <rect x="0" y="182" width="461" height="2.5" class="f-blue"/>
  <text x="102" y="160" font-size="32" letter-spacing="2.5" class="f-white">Insert Title</text>
  <circle cx="78" cy="222" r="13" class="f-blue"/>
  <text x="96" y="232" font-size="30" class="brand-name">korvet</text>
  <text x="262" y="221" font-size="8" letter-spacing="3" class="f-ink">TEXT GOES HERE</text>
</svg>

<!-- Agenda -->
<svg class="slide row-1 col-2" viewBox="0 0 461 259">
  <line x1="0" y1="43" x2="131" y2="43" class="s-blue" stroke-width="1"/>
  <text x="141" y="47" class="slide-title">AGENDA STYLE</text>
  <g>
    <rect x="86" y="64" width="47" height="24" rx="12" class="f-sky"/>
    <rect x="86" y="95.5" width="47" height="24" rx="12" class="f-deep"/>
    <rect x="86" y="127" width="47" height="24" rx="12" class="f-teal"/>
    <rect x="86" y="158.5" width="47" height="24" rx="12" class="f-green"/>
    <rect x="86" y="190" width="47" height="24" rx="12" class="f-grey"/>
    <g font-size="14" class="f-white">
      <text x="108" y="81">1</text><text x="108" y="112.5">2</text><text x="108" y="144">3</text><text x="108" y="175.5">4</text><text x="108" y="207">5</text>
    </g>
    <g fill="none" stroke="#555" stroke-width="0.7">
      <rect x="141" y="64" width="235" height="24"/><rect x="141" y="95.5" width="235" height="24"/>
      <rect x="141" y="127" width="235" height="24"/><rect x="141" y="158.5" width="235" height="24"/>
      <rect x="141" y="190" width="235" height="24"/>
    </g>
    <rect x="382" y="64" width="3" height="24" class="f-sky"/>
    <rect x="382" y="95.5" width="3" height="24" class="f-deep"/>
    <rect x="382" y="127" width="3" height="24" class="f-teal"/>
    <rect x="382" y="158.5" width="3" height="24" fill="#c8c8c8"/>
    <rect x="382" y="190" width="3" height="24" class="f-grey"/>
    <g class="f-ink">
      <text x="157" y="75" font-size="7" letter-spacing="0.8">CONTENT TITLE</text><text x="157" y="82" class="caption">You can change this paragraph and add your text in here</text>
      <text x="157" y="106.5" font-size="7" letter-spacing="0.8">CONTENT TITLE</text><text x="157" y="113.5" class="caption">You can change this paragraph and add your text in here</text>
      <text x="157" y="138" font-size="7" letter-spacing="0.8">CONTENT TITLE</text><text x="157" y="145" class="caption">You can change this paragraph and add your text in here</text>
      <text x="157" y="169.5" font-size="7" letter-spacing="0.8">CONTENT TITLE</text><text x="157" y="176.5" class="caption">You can change this paragraph and add your text in here</text>
      <text x="157" y="201" font-size="7" letter-spacing="0.8">CONTENT TITLE</text><text x="157" y="208" class="caption">You can change this paragraph and add your text in here</text>
    </g>
  </g>
  <use href="#brand-small" x="41" y="232" width="70" height="18"/>
  <rect x="201" y="240" width="260" height="8" fill="url(#footer-fade)" role="img" aria-label="Circuit trace decoration"/>
</svg>

<!-- Section divider 01 -->
<svg class="slide row-1 col-3" viewBox="0 0 461 259">
  <text x="40" y="126" class="divider-number f-blue">01</text>
  <text x="41" y="142" class="divider-label">SECTION DIVIDER</text>
  <text x="41" y="151" class="caption">You can add your text in here</text>
  <g>
    <rect x="325" y="40" width="34" height="20" fill="#4a6f85"/>
    <rect x="276" y="87" width="38" height="29" fill="#a8877a" role="img" aria-label="Photo of a smiling colleague"/>
    <rect x="324" y="70" width="66" height="94" fill="#6b4b3c" role="img" aria-label="Photo of a smiling young woman"/>
    <rect x="202" y="124" width="54" height="49" fill="#57606a" role="img" aria-label="Photo of a young man laughing"/>
    <rect x="266" y="124" width="48" height="49" fill="#8798a6" role="img" aria-label="Photo of a team at work"/>
    <rect x="400" y="112" width="53" height="52" fill="#4a6f85"/>
    <rect x="202" y="182" width="28" height="28" fill="#8c6e66" role="img" aria-label="Photo detail of a colleague"/>
    <rect x="236" y="182" width="78" height="77" fill="#5d5046" role="img" aria-label="Photo of students studying with books"/>
    <rect x="324" y="174" width="86" height="85" fill="#8fa9b8" role="img" aria-label="Photo of a woman working on a laptop"/>
    <rect x="419" y="174" width="34" height="38" fill="#5f8aa3" role="img" aria-label="Photo detail of an office"/>
  </g>
  <use href="#brand-small" x="41" y="232" width="70" height="18"/>
</svg>

<!-- Section divider 02 -->
<svg class="slide row-2 col-1" viewBox="0 0 461 259">
  <text x="40" y="126" class="divider-number f-green">02</text>
  <text x="41" y="142" class="divider-label">SECTION DIVIDER</text>
  <text x="41" y="151" class="caption">You can add your text in here</text>
  <g>
    <rect x="324" y="40" width="35" height="20" fill="#7a3a2a"/>
    <rect x="276" y="87" width="38" height="28" fill="#c9b3a8" role="img" aria-label="Photo of a hand on a document"/>
    <rect x="324" y="69" width="66" height="94" fill="#c58d6d" role="img" aria-label="Photo of a hand pointing at a report"/>
    <rect x="400" y="112" width="53" height="51" fill="#e7e2e2" role="img" aria-label="Photo of printed charts"/>
    <rect x="201" y="125" width="56" height="48" fill="#b9cde4" role="img" aria-label="Photo of a bar chart report"/>
    <rect x="265" y="125" width="49" height="48" fill="#a9c0df" role="img" aria-label="Photo of a bar chart report"/>
    <rect x="201" y="181" width="28" height="28" fill="#d7e2ee" role="img" aria-label="Photo detail of a chart"/>
    <rect x="237" y="181" width="77" height="77" fill="#6d93cf" role="img" aria-label="Photo of blue bar charts"/>
    <rect x="324" y="173" width="86" height="85" fill="#cfd7e2" role="img" aria-label="Photo of a pen over financial charts"/>
    <rect x="419" y="173" width="34" height="39" fill="#e1e7ef" role="img" aria-label="Photo detail of a chart"/>
  </g>
  <use href="#brand-small" x="41" y="232" width="70" height="18"/>
</svg>

<!-- Section divider 03 -->
<svg class="slide row-2 col-2" viewBox="0 0 461 259">
  <text x="40" y="126" class="divider-number" fill="#555">03</text>
  <text x="41" y="142" class="divider-label">SECTION DIVIDER</text>
  <text x="41" y="151" class="caption">You can add your text in here</text>
  <defs>
    <linearGradient id="network-tone" x1="0" y1="0" x2="1" y2="1">
      <stop offset="0" stop-color="#1d6fb0"/><stop offset="1" stop-color="#0a2c55"/>
    </linearGradient>
  </defs>
  <g fill="url(#network-tone)">
    <rect x="324" y="40" width="35" height="20" role="img" aria-label="Abstract blue network image"/>
    <rect x="275" y="87" width="39" height="28" fill="#2b78b7"/>
    <rect x="324" y="69" width="67" height="94" role="img" aria-label="Abstract blue network image"/>
    <rect x="400" y="112" width="52" height="51" role="img" aria-label="Abstract blue network image"/>
    <rect x="201" y="125" width="56" height="48" role="img" aria-label="Abstract blue network image"/>
    <rect x="265" y="125" width="49" height="48" role="img" aria-label="Abstract blue network image"/>
    <rect x="201" y="181" width="28" height="28" role="img" aria-label="Abstract blue network image"/>
    <rect x="237" y="181" width="77" height="77" role="img" aria-label="Abstract blue network image"/>
    <rect x="324" y="173" width="85" height="85" role="img" aria-label="Abstract blue network image"/>
    <rect x="419" y="173" width="33" height="39" role="img" aria-label="Abstract blue network image"/>
  </g>
  <use href="#brand-small" x="41" y="232" width="70" height="18"/>
</svg>

<!-- Content -->
<svg class="slide row-2 col-3" viewBox="0 0 461 259">
  <line x1="0" y1="40" x2="132" y2="40" class="s-blue" stroke-width="1"/>
  <text x="142" y="46" class="slide-title">CONTENT SLIDE</text>
  <g>
    <text x="124" y="83" class="menu-item f-deep">ABOUT US</text><text x="124" y="91" class="caption">You can add your text in here</text>
    <text x="124" y="115" class="menu-item f-teal">SERVICES</text><text x="124" y="123" class="caption">You can add your text in here</text>
    <text x="124" y="148" class="menu-item f-blue">OUR TEAM</text><text x="124" y="156" class="caption">You can add your text in here</text>
    <text x="124" y="181" class="menu-item f-grey">IDEAS</text><text x="124" y="189" class="caption">You can add your text in here</text>
    <text x="260" y="83" class="menu-item f-grey">CAREERS</text><text x="260" y="91" class="caption">You can add your text in here</text>
    <text x="260" y="115" class="menu-item f-green">ANALYSIS</text><text x="260" y="123" class="caption">You can add your text in here</text>
    <text x="260" y="148" class="menu-item f-deep">NEWS</text><text x="260" y="156" class="caption">You can add your text in here</text>
    <text x="260" y="181" class="menu-item f-blue">CONTACT</text><text x="260" y="189" class="caption">You can add your text in here</text>
  </g>
  <use href="#brand-small" x="41" y="232" width="70" height="18"/>
  <rect x="201" y="240" width="260" height="8" fill="url(#footer-fade)" role="img" aria-label="Circuit trace decoration"/>
</svg>

<!-- White -->
<svg class="slide row-3 col-1" viewBox="0 0 461 259">
  <use href="#brand-small" x="41" y="232" width="70" height="18"/>
  <rect x="201" y="238" width="260" height="8" fill="url(#footer-fade)" role="img" aria-label="Circuit trace decoration"/>
</svg>

<!-- Comparison -->
<svg class="slide row-3 col-2" viewBox="0 0 461 259">
  <line x1="0" y1="42" x2="131" y2="42" class="s-blue" stroke-width="1"/>
  <text x="141" y="47" class="slide-title">COMPARISON SLIDE</text>
  <rect x="71" y="66" width="96" height="18" class="f-blue"/>
  <rect x="183" y="66" width="96" height="18" fill="#7a7a7a"/>
  <rect x="295" y="66" width="96" height="18" fill="#2e9d92"/>
  <text x="119" y="78" text-anchor="middle" class="head-text">TWO</text>
  <text x="231" y="78" text-anchor="middle" class="head-text">THREE</text>
  <text x="343" y="78" text-anchor="middle" class="head-text">FOUR</text>
  <g class="f-soft">
    <rect x="71" y="90" width="96" height="24"/><rect x="71" y="119" width="96" height="24"/>
    <rect x="183" y="90" width="96" height="24"/><rect x="183" y="119" width="96" height="24"/><rect x="183" y="148" width="96" height="24"/>
    <rect x="295" y="90" width="96" height="24"/><rect x="295" y="119" width="96" height="24"/><rect x="295" y="148" width="96" height="24"/><rect x="295" y="177" width="96" height="24"/>
  </g>
  <g class="cell-text">
    <text x="79" y="103">Text in here</text><text x="79" y="132">Text in here</text>
    <text x="191" y="103">Text in here</text><text x="191" y="132">Text in here</text><text x="191" y="161">Text in here</text>
    <text x="303" y="103">Text in here</text><text x="303" y="132">Text in here</text><text x="303" y="161">Text in here</text><text x="303" y="190">Text in here</text>
  </g>
  <line x1="71" y1="208" x2="391" y2="208" class="s-soft" stroke-width="1"/>
  <text x="71" y="218" class="caption">You can change this paragraph and add your text in here</text>
  <use href="#brand-small" x="41" y="232" width="70" height="18"/>
  <rect x="201" y="238" width="260" height="8" fill="url(#footer-fade)" role="img" aria-label="Circuit trace decoration"/>
</svg>

<!-- Table -->
<svg class="slide row-3 col-3" viewBox="0 0 461 259">
  <line x1="0" y1="42" x2="132" y2="42" class="s-blue" stroke-width="1"/>
  <text x="142" y="47" class="slide-title">TABLE SLIDE</text>
  <g fill="none" stroke-width="0.8">
    <rect x="70" y="66" width="321" height="142" stroke="#bbb"/>
    <line x1="150" y1="66" x2="150" y2="208" class="s-blue"/>
    <line x1="230" y1="66" x2="230" y2="208" class="s-teal"/>
    <line x1="310" y1="66" x2="310" y2="208" class="s-green"/>
    <g stroke="#bbb">
      <line x1="70" y1="110" x2="391" y2="110"/><line x1="70" y1="134.5" x2="391" y2="134.5"/>
      <line x1="70" y1="159" x2="391" y2="159"/><line x1="70" y1="183.5" x2="391" y2="183.5"/>
    </g>
  </g>
  <rect x="70" y="66" width="80" height="2" class="f-blue"/><rect x="150" y="66" width="80" height="2" class="f-teal"/>
  <rect x="230" y="66" width="80" height="2" class="f-green"/><rect x="310" y="66" width="81" height="2" class="f-grey"/>
  <rect x="75" y="68" width="70" height="12" class="f-blue"/><rect x="155" y="68" width="70" height="12" class="f-teal"/>
  <rect x="235" y="68" width="70" height="12" class="f-green"/><rect x="315" y="68" width="70" height="12" class="f-grey"/>
  <g class="head-text" text-anchor="middle">
    <text x="110" y="77">CONTENT</text><text x="190" y="77">CONTENT</text><text x="270" y="77">CONTENT</text><text x="350" y="77">CONTENT</text>
  </g>
  <g class="cell-text">
    <text x="80" y="99">Text in here</text><text x="160" y="99">Text in here</text><text x="240" y="99">Text in here</text><text x="320" y="99">Text in here</text>
    <text x="80" y="124">Text in here</text><text x="160" y="124">Text in here</text><text x="240" y="124">Text in here</text><text x="320" y="124">Text in here</text>
    <text x="80" y="148">Text in here</text><text x="160" y="148">Text in here</text><text x="240" y="148">Text in here</text><text x="320" y="148">Text in here</text>
    <text x="80" y="173">Text in here</text><text x="160" y="173">Text in here</text><text x="240" y="173">Text in here</text><text x="320" y="173">Text in here</text>
    <text x="80" y="197">Text in here</text><text x="160" y="197">Text in here</text><text x="240" y="197">Text in here</text><text x="320" y="197">Text in here</text>
  </g>
  <use href="#brand-small" x="41" y="232" width="70" height="18"/>
  <rect x="201" y="238" width="260" height="8" fill="url(#footer-fade)" role="img" aria-label="Circuit trace decoration"/>
</svg>

<!-- Timeline -->
<svg class="slide row-4 col-4a" viewBox="0 0 461 259">
  <line x1="0" y1="40" x2="132" y2="40" class="s-blue" stroke-width="1"/>
  <text x="142" y="46" class="slide-title">TIMELINE SLIDE</text>
  <line x1="42" y1="145" x2="414" y2="145" stroke="#ccc" stroke-width="0.8"/>
  <g stroke-width="0.7" fill="none">
    <line x1="93" y1="62" x2="143" y2="62" stroke="#ccc"/><line x1="203" y1="62" x2="253" y2="62" stroke="#ccc"/><line x1="310" y1="62" x2="364" y2="62" stroke="#ccc"/>
    <line x1="120" y1="94" x2="120" y2="138" class="s-blue"/>
    <line x1="230" y1="94" x2="230" y2="138" class="s-teal"/>
    <line x1="338" y1="94" x2="338" y2="138" class="s-grey"/>
    <line x1="175" y1="152" x2="175" y2="196" class="s-blue"/>
    <line x1="283" y1="152" x2="283" y2="196" class="s-green"/>
    <line x1="148" y1="222" x2="202" y2="222" class="s-blue" stroke-width="1"/>
    <line x1="256" y1="222" x2="310" y2="222" class="s-green" stroke-width="1"/>
    <circle cx="120" cy="145" r="12" stroke="#ccc"/><circle cx="120" cy="145" r="7" class="s-blue"/>
    <circle cx="175" cy="145" r="12" stroke="#ccc"/><circle cx="175" cy="145" r="7" class="s-blue"/>
    <circle cx="230" cy="145" r="12" stroke="#ccc"/><circle cx="230" cy="145" r="7" class="s-teal"/>
    <circle cx="283" cy="145" r="12" stroke="#ccc"/><circle cx="283" cy="145" r="7" class="s-green"/>
    <circle cx="338" cy="145" r="12" stroke="#ccc"/><circle cx="338" cy="145" r="7" class="s-grey"/>
  </g>
  <circle cx="120" cy="94" r="1.5" class="f-blue"/><circle cx="230" cy="94" r="1.5" class="f-teal"/><circle cx="338" cy="94" r="1.5" class="f-grey"/>
  <circle cx="175" cy="196" r="1.5" class="f-blue"/><circle cx="283" cy="196" r="1.5" class="f-green"/>
  <circle cx="120" cy="145" r="4" class="f-blue"/><circle cx="175" cy="145" r="4" class="f-deep"/>
  <circle cx="230" cy="145" r="4" class="f-teal"/><circle cx="283" cy="145" r="4" class="f-green"/>
  <circle cx="338" cy="145" r="4" class="f-grey"/>
  <g class="cell-text">
    <text x="93" y="71">Text in here</text><text x="203" y="71">Text in here</text><text x="310" y="71">Text in here</text>
    <text x="148" y="212">Text in here</text><text x="256" y="212">Text in here</text>
  </g>
  <text x="120" y="176" text-anchor="middle" class="year f-blue">2015</text>
  <text x="175" y="128" text-anchor="middle" class="year f-deep">2016</text>
  <text x="230" y="176" text-anchor="middle" class="year f-teal">2017</text>
  <text x="283" y="128" text-anchor="middle" class="year f-green">2018</text>
  <text x="338" y="176" text-anchor="middle" class="year f-grey">2019</text>
  <use href="#brand-small" x="41" y="232" width="70" height="18"/>
  <rect x="201" y="238" width="260" height="8" fill="url(#footer-fade)" role="img" aria-label="Circuit trace decoration"/>
</svg>

<!-- End -->
<svg class="slide row-4 col-4b" viewBox="0 0 461 259">
  <rect x="100" y="40" width="261" height="190" fill="url(#ring-fade)" role="img" aria-label="Circuit board ring decoration around the company name"/>
  <circle cx="191" cy="132" r="13" class="f-blue"/>
  <text x="209" y="142" font-size="30" class="brand-name">korvet</text>
</svg>

</body>
</html>
```